Re-Design of a 1 Pager IT Security Website

Please create a 1 Pager design for this website and all its elements: http://www.pelmarokvistaqueen.com/

Colours, Fonts etc: You can select whatever you prefer

```html
<!DOCTYPE html>
<html lang="en">
<head>
<meta charset="utf-8">
<title>Velqora – Domain Monitoring</title>
<link href="https://fonts.googleapis.com/css2?family=Catamaran:wght@300;400;500;600;700;800&display=swap" rel="stylesheet">
<style>
:root{
  --gold:#e8bf45;
  --gold-soft:#efcd64;
  --ink:#1f1f1f;
  --text:#555;
  --dark:#1e1e1e;
  --footer:#2b2b2b;
  --white:#fff;
  --line:#e6e6e6;
  --navy:#07111d;
}
*{box-sizing:border-box;margin:0;padding:0}
html,body{width:1200px;height:3215px;overflow:hidden}
body{position:relative;background:var(--white);font-family:"Catamaran",sans-serif;color:var(--text)}
.abs{position:absolute}
.center{left:0;width:1200px;text-align:center}
.badge{display:inline-block;border:1px solid var(--gold);color:var(--gold);font-size:9px;font-weight:700;letter-spacing:2.5px;padding:6px 18px;text-transform:uppercase}
.eyebrow{color:var(--gold);font-size:10px;font-weight:600;letter-spacing:3px;text-transform:uppercase;display:flex;align-items:center;gap:10px}
.eyebrow::after{content:"";width:16px;height:1px;background:var(--gold)}
.pill{display:inline-block;border-radius:20px;font-size:9.5px;letter-spacing:1.5px;text-transform:uppercase;padding:0 20px;line-height:32px;font-weight:500}
.pill--gold{background:var(--gold);color:var(--white)}
.pill--white{background:var(--white);color:#444}
h2{font-weight:700;color:var(--ink);font-size:28px;line-height:34px;letter-spacing:.3px;text-transform:uppercase}

/* hero */
.hero{top:0;left:0;width:1200px;height:571px;background:radial-gradient(ellipse at 30% 60%,#0f4f73 0%,transparent 45%),radial-gradient(ellipse at 80% 40%,#0b5d80 0%,transparent 40%),linear-gradient(180deg,#04070c 0%,#0a1b2a 55%,#081320 100%)}
.hero__title{top:222px;color:var(--white);font-size:34px;font-weight:800;line-height:38px;text-transform:uppercase}
.hero__sub{top:308px;color:var(--white);font-size:10px}
.hero__btn{top:341px}
.hero__down{top:520px;left:582px;width:28px;height:28px;border-radius:50%;background:rgba(255,255,255,.15);display:flex;align-items:center;justify-content:center}

/* risk */
.risk__media{top:649px;left:72px;width:516px;height:344px;background:radial-gradient(ellipse at 65% 55%,#3ea0ff 0%,#0d4fb0 35%,#061b46 100%)}
.risk__play{top:784px;left:552px;width:72px;height:72px;border-radius:50%;background:var(--gold);box-shadow:0 6px 14px rgba(0,0,0,.25);display:flex;align-items:center;justify-content:center}
.risk__copy{top:651px;left:659px;width:370px}
.risk__copy h2{margin:12px 0 14px}
.risk__copy p{font-size:11.5px;line-height:19px;margin-bottom:8px;font-weight:300;color:#444}
.risk__copy .pill{margin-top:24px}

/* divider */
.divider{top:1064px;left:0;width:1200px;display:flex;align-items:center;justify-content:center;gap:22px}
.divider span{color:var(--gold);font-size:10px;letter-spacing:4px;text-transform:uppercase}
.divider::before,.divider::after{content:"";flex:1;height:1px;background:var(--line)}

/* attack types */
.type{width:320px;text-align:center}
.type__photo{margin:0 auto;width:168px;height:168px;border-radius:50%;position:relative}
.type__icon{position:absolute;right:40px;bottom:-14px;width:46px;height:46px;border-radius:50%;background:var(--white);box-shadow:0 2px 6px rgba(0,0,0,.15);display:flex;align-items:center;justify-content:center}
.type h3{font-size:15px;font-weight:700;color:var(--ink);text-transform:uppercase;letter-spacing:.4px;margin:40px 0 6px}
.type p{font-size:11.5px;line-height:19px;font-weight:300;color:#444}

/* protection */
.protect__media{top:1655px;left:177px;width:951px;height:534px;background:linear-gradient(120deg,#3c6a63 0%,#7fb0b0 30%,#2e5f6a 55%,#1a3346 80%,#0f1e2b 100%)}
.protect__card{top:1823px;left:60px;width:540px;height:325px;background:var(--dark);border-bottom:2px solid var(--gold);padding:46px 48px}
.protect__card h2{color:var(--white);margin:14px 0 12px}
.protect__card p{color:#ddd;font-size:11.5px;line-height:19px;font-weight:300}
.protect__card a{color:var(--gold);text-decoration:none}
.protect__card .note{margin-top:10px}
.protect__card .actions{margin-top:16px;display:flex;gap:10px;padding-left:4px}

/* monitoring */
.monitor__eyebrow{top:2270px;display:flex;justify-content:center}
.monitor__eyebrow .eyebrow::before{content:"";width:16px;height:1px;background:var(--gold)}
.monitor__title{top:2293px}
.monitor__text{top:2342px;left:344px;width:512px;text-align:center;font-size:11.5px;line-height:19px;font-weight:300;color:#444}
.monitor__text p+p{margin-top:8px}
.feature{top:2496px;width:270px;text-align:center}
.feature__icon{margin:0 auto;width:80px;height:80px;border-radius:50%;background:#efefef;display:flex;align-items:center;justify-content:center}
.feature--active .feature__icon{background:var(--gold)}
.feature h4{margin-top:18px;font-size:12px;font-weight:700;color:var(--ink);text-transform:uppercase;letter-spacing:.3px}
.feature--active h4{color:var(--gold)}
.feature span{font-size:11.5px;font-weight:300;color:#444}

/* contact */
.contact{top:2728px;left:0;width:1200px;height:300px;background:radial-gradient(ellipse at 20% 30%,#263a66 0%,transparent 50%),linear-gradient(180deg,#141d3a 0%,#0b1228 100%)}
.contact__label{top:2791px;display:flex;justify-content:center}
.contact__label .eyebrow{font-size:8px}
.contact__label .eyebrow::before{content:"";width:14px;height:1px;background:var(--gold)}
.contact__title{top:2808px;color:var(--white)!important;font-size:22px;line-height:28px}
.contact__text{top:2850px;left:370px;width:460px;text-align:center;color:var(--white);font-size:9.5px;line-height:15px}
.contact__actions{top:2933px;display:flex;justify-content:center;gap:10px}
.contact__actions .pill{font-size:8px;line-height:26px;padding:0 16px}

/* footer */
.footer{top:3028px;left:0;width:1200px;height:187px;background:var(--footer)}
.footer__badge{top:3066px}
.footer__copy{top:3103px;color:#aaa;font-size:8px;letter-spacing:.6px}
.footer__links{top:3124px;display:flex;justify-content:center;gap:22px;font-size:8px;color:#ddd;letter-spacing:.6px}
.footer__social{top:3158px;display:flex;justify-content:center;gap:20px}
.footer__social i{width:9px;height:9px;border-radius:50%;background:#e8e8e8;display:block}
.footer__up{top:3192px}
</style>
</head>
<body>

<section class="hero abs" role="img" aria-label="Glowing blue digital number grid background"></section>
<div class="abs center" style="top:187px"><span class="badge">Domain Monitoring</span></div>
<h1 class="abs center hero__title">Prevent attacks by<br>monitoring your domains</h1>
<p class="abs center hero__sub">Our domain monitoring solution continuously monitors thousands of TLDs, gTLDs and ccTLDs.</p>
<div class="abs center hero__btn"><span class="pill pill--gold" style="line-height:26px;font-size:8px">Explore more</span></div>
<div class="abs hero__down"><svg width="10" height="10" viewBox="0 0 10 10"><path d="M2 3.5l3 3 3-3" fill="none" stroke="#fff" stroke-width="1.2"/></svg></div>

<div class="abs risk__media" role="img" aria-label="Code overlay on a blue lit server room corridor"></div>
<div class="abs risk__play"><svg width="22" height="22" viewBox="0 0 22 22"><path d="M5 3l14 8-14 8z" fill="none" stroke="#fff" stroke-width="1.6"/></svg></div>
<div class="abs risk__copy">
  <div class="eyebrow">Attacks</div>
  <h2>What is the risk?</h2>
  <p>Hackers use domain-based attacks, which are designed to trick users into submitting sensitive data or downloading dangerous files. This is often the case with phishing attacks.</p>
  <p>For example, domains can be registered that are very similar to one's own company, a customer or a supplier.</p>
  <p>Once a fraudulent domain is registered, the hackers try to lure the employee to the website. This can be done via e-mail, SMS (smishing), instant messaging. Social media and many other techniques succeed.</p>
  <span class="pill pill--gold">Learn more</span>
</div>

<div class="abs divider"><span>Types of attacks</span></div>

<div class="abs type" style="top:1155px;left:80px">
  <div class="type__photo" role="img" aria-label="Purple and blue streaming code" style="background:radial-gradient(circle at 55% 45%,#5a6cf0 0%,#3a2a9a 55%,#1a1050 100%)">
    <div class="type__icon"><svg width="18" height="18" viewBox="0 0 18 18" fill="none" stroke="#333" stroke-width="1"><circle cx="9" cy="9" r="7"/><ellipse cx="9" cy="9" rx="3" ry="7"/><path d="M2 9h14M3 5.5h12M3 12.5h12"/></svg></div>
  </div>
  <h3>Domain spoofing</h3>
  <p>Here, a domain name is registered that resembles that of a trusted brand or organization. For example, the hacker can register the domain "tapcal-access.services" and lure the victim to the website under a certain pretext. At the same time, the original website can also be copied 1:1, so that visually there is no difference.</p>
</div>

<div class="abs type" style="top:1155px;left:440px">
  <div class="type__photo" role="img" aria-label="Dark shield emblem with a gold database badge" style="background:radial-gradient(circle,#4a4a4a 0%,#222 70%);border:3px solid #fff;box-shadow:0 0 0 1px #ddd">
    <div style="position:absolute;left:61px;top:61px;width:40px;height:40px;border-radius:50%;background:var(--gold);display:flex;align-items:center;justify-content:center"><svg width="16" height="18" viewBox="0 0 16 18" fill="none" stroke="#fff" stroke-width="1.2"><ellipse cx="8" cy="4" rx="6" ry="2.5"/><path d="M2 4v10c0 1.4 2.7 2.5 6 2.5s6-1.1 6-2.5V4M2 9c0 1.4 2.7 2.5 6 2.5s6-1.1 6-2.5"/></svg></div>
  </div>
  <h3 style="margin-top:24px">Homoglyphic attack</h3>
  <p>This is a variant of domain spoofing. Again, a similar looking domain is registered to. But one uses characters outside the Latin alphabet in the domain name that resemble the corresponding characters in the URL of the target domain. Replacing the "g" with q is also very popular. Multi-letter homoglyphs are also popular, e.g. "rn" instead of "m". In more complex scenarios, homoglyphs can also be generated with the use of different alphabets and special characters.</p>
</div>

<div class="abs type" style="top:1155px;left:799px">
  <div class="type__photo" role="img" aria-label="Digital padlock in a glowing circuit ring" style="background:radial-gradient(circle,#7a9ad8 0%,#3a4f8a 40%,#5a4a78 70%,#2a2440 100%)">
    <div class="type__icon"><svg width="18" height="18" viewBox="0 0 18 18" fill="none" stroke="#333" stroke-width="1"><rect x="3" y="3" width="9" height="9"/><rect x="6" y="6" width="9" height="9" fill="#fff"/></svg></div>
  </div>
  <h3>Typosquatting</h3>
  <p>Cybercriminals may attempt to register a malicious domain by using a common misspelling of the target company's domain. For example, someone might reserve "tapcak.com" because the letter "L" and "K" are next to each other at the keyboard. If a customer of the target company misspells the domain, he will land on the fraudulent domain where he can become a victim of cybercriminals.</p>
</div>

<div class="abs protect__media" role="img" aria-label="Binary digits rising over a city skyline and laptop"></div>
<div class="abs protect__card">
  <div class="eyebrow">Protection</div>
  <h2>How to protect yourself?</h2>
  <p>Our domain monitoring solution continuously monitors thousands of TLDs, gTLDs and ccTLDs. For searches, we offer the greatest flexibility in the market and cover ALL forms of attacks. Here are a few examples of search options that can be adopted as active alerts: <a href="#">https://docs.velqora.io/guide/domain_database_search</a></p>
  <p class="note">All data can be</p>
  <div class="actions"><span class="pill pill--gold" style="padding:0 22px">Analyzed</span><span class="pill pill--white" style="padding:0 20px">Exported</span></div>
</div>

<div class="abs center monitor__eyebrow"><div class="eyebrow">Monitoring</div></div>
<h2 class="abs center monitor__title">What else are we monitoring?</h2>
<div class="abs monitor__text">
  <p>Velqora helps you understand when, where and how stolen or accidentally leaked information in dark web markets, forums, botnet logs, IRC, social media and other sources is exposed. Velqora's alerting service can also detect threats before they turn into incidents. Velqora offers AI-driven dark web analysis, real-time threat alerts and pre-Attack threat indicators.</p>
  <p>Setup in minutes you will receive instant access to real-time reporting including:</p>
</div>

<div class="abs feature" style="left:60px">
  <div class="feature__icon"><svg width="30" height="30" viewBox="0 0 30 30" fill="none" stroke="#444" stroke-width="1.1"><circle cx="15" cy="15" r="9"/><circle cx="15" cy="15" r="3"/><path d="M15 3v5M15 22v5M3 15h5M22 15h5"/></svg></div>
  <h4>Infrastructure exposure</h4><span>IOT, Gitrova, Cloudnexa &amp; more</span>
</div>
<div class="abs feature feature--active" style="left:330px">
  <div class="feature__icon"><svg width="30" height="30" viewBox="0 0 30 30" fill="none" stroke="#fff" stroke-width="1.1"><circle cx="15" cy="12" r="5"/><path d="M7 25c1-5 4-7 8-7s7 2 8 7M4 6l3 2M26 6l-3 2"/></svg></div>
  <h4>People exposure</h4><span>Social media monitoring</span>
</div>
<div class="abs feature" style="left:599px">
  <div class="feature__icon"><svg width="30" height="30" viewBox="0 0 30 30" fill="none" stroke="#444" stroke-width="1.1"><rect x="5" y="6" width="20" height="14"/><path d="M3 24h24"/><rect x="12" y="11" width="6" height="5"/><path d="M13 11V9a2 2 0 014 0v2"/></svg></div>
  <h4>Ransomware exposure</h4><span>leak &amp; credential monitoring</span>
</div>
<div class="abs feature" style="left:869px">
  <div class="feature__icon"><svg width="30" height="30" viewBox="0 0 30 30" fill="none" stroke="#444" stroke-width="1.1"><rect x="6" y="6" width="18" height="18"/><circle cx="15" cy="15" r="4"/><path d="M3 10h3M3 20h3M24 10h3M24 20h3M10 3v3M20 3v3M10 24v3M20 24v3"/></svg></div>
  <h4>Attack prevention</h4><span>domain and certificate monitoring</span>
</div>

<section class="abs contact" role="img" aria-label="Blurred code editor on a dark navy screen"></section>
<div class="abs center contact__label"><div class="eyebrow">Contact</div></div>
<h2 class="abs center contact__title">Want to know more?</h2>
<p class="abs contact__text">Velqora (company registration number CHE-418.207.615) was started in 2016 as a public limited company in Lindavik, Nordmark. Our analysts have long-standing relationships with various players on the Darknet. These personal relationships make it possible for Velqora to repeatedly obtain the latest data leaks. Those unique data leaks are published by the press around the world.</p>
<div class="abs center contact__actions"><span class="pill pill--gold">Contact us!</span><span class="pill pill--white">More about us</span></div>

<footer class="abs footer"></footer>
<div class="abs center footer__badge"><span class="badge" style="font-size:8.5px">Domain Monitoring</span></div>
<p class="abs center footer__copy">© 2022 VELQORAJO. ALL RIGHTS RESERVED</p>
<div class="abs center footer__links"><span>TERMS AND CONDITIONS</span><span>PRIVACY POLICY</span></div>
<div class="abs center footer__social"><i></i><i></i><i></i><i></i></div>
<div class="abs center footer__up"><svg width="10" height="8" viewBox="0 0 10 8"><path d="M1 6l4-4 4 4" fill="none" stroke="#888" stroke-width="1.2"/></svg></div>

</body>
</html>
```